Creative Business Card for my Sail Boat.. Tide & Time

Going to order PLASTIC business cards for my boat.. she is a sailing vessel catamaran named Tide & Time..

Target Market(s)

to impress other boaters with a unique designed plastic card

Contact Information for Business Card

S/V Tide & Time
Captain Tom Harlow
harlow@tom.example
Mobile/WhatsApp 1-555-318-7062
www.sailtideandtime.example

Requirements
Must have
• Cool colors. logo.. and info in Business Card Details.. Thanks! Utilize clear or cloudy plastic in design. Thanks

```html
<!DOCTYPE html>
<html lang="en">
<head>
<meta charset="utf-8">
<title>Tide &amp; Time – Business Card</title>
<link rel="stylesheet" href="https://fonts.googleapis.com/css2?family=Arimo:wght@400;700&display=swap">
<style>
  :root {
    --page: #ecebe8;
    --card-red: #c62128;
    --sail-green: #319c46;
    --frost-light: #fbfafa;
    --frost-shade: #d8cfcb;
    --ink-white: #ffffff;
    --mark-brown: #5b3d31;
  }
  * { margin: 0; padding: 0; box-sizing: border-box; }
  html, body {
    width: 1200px; height: 900px; overflow: hidden;
    background: var(--page);
    font-family: "Arimo", Arial, sans-serif;
  }
  .business-card {
    position: absolute; left: 100px; top: 141px;
    width: 1000px; height: 618px;
    background: var(--card-red);
    overflow: hidden;
    box-shadow: 0 10px 30px rgba(0,0,0,.18);
  }
  .card-art { position: absolute; inset: 0; width: 100%; height: 100%; }
  .owner { position: absolute; left: 49px; top: 70px; color: var(--ink-white); }
  .owner-name { font-size: 45px; font-weight: 700; letter-spacing: .5px; line-height: 1; }
  .owner-role { font-size: 28px; font-weight: 400; margin-top: 4px; }
  .contact-list {
    position: absolute; left: 49px; top: 400px; list-style: none;
    color: var(--ink-white); font-size: 27px;
  }
  .contact-item { display: flex; align-items: center; height: 37.5px; }
  .contact-icon { width: 32px; height: 30px; margin-right: 12px; flex: none; }
  .vessel-mark {
    position: absolute; left: 480px; top: 192px; width: 380px;
    text-align: center; color: var(--mark-brown);
    font-weight: 700; font-size: 80px; line-height: 1.08;
  }
  .vessel-mark-dot {
    display: inline-block; width: 46px; height: 46px; border-radius: 50%;
    background: var(--sail-green); margin-left: 10px; vertical-align: middle;
  }
</style>
</head>
<body>
  <div class="business-card">
    <svg class="card-art" viewBox="0 0 1090 673" preserveAspectRatio="none" aria-hidden="true">
      <defs>
        <radialGradient id="frost" cx="50%" cy="45%" r="60%">
          <stop offset="0%" stop-color="var(--frost-light)"/>
          <stop offset="100%" stop-color="var(--frost-shade)"/>
        </radialGradient>
      </defs>
      <path class="green-corner" fill="var(--sail-green)" d="M600,0 L1090,0 L1090,673 L740,673 Z"/>
      <path class="heart-frame" fill="var(--card-red)"
        d="M731,85 C790,25 850,0 900,0 C1010,0 1085,80 1088,220 C1090,380 900,560 720,700 L300,700 L300,0 L620,0 C660,20 700,50 731,85 Z"/>
      <path class="clear-heart" fill="url(#frost)"
        d="M731,188 C680,120 630,65 570,65 C490,65 439,130 439,215 C439,330 600,470 731,598 C862,470 1021,330 1021,215 C1021,130 970,65 890,65 C830,65 780,120 731,188 Z"/>
    </svg>

    <div class="owner">
      <div class="owner-name">TOM HARLOW</div>
      <div class="owner-role">Captain</div>
    </div>

    <div class="vessel-mark">Tide &amp;<span class="vessel-mark-dot"></span><br>Time</div>

    <ul class="contact-list">
      <li class="contact-item">
        <svg class="contact-icon" viewBox="0 0 32 30"><rect x="2" y="7" width="28" height="18" fill="#fff"/><path d="M2,7 L16,18 L30,7" fill="none" stroke="var(--card-red)" stroke-width="2"/></svg>
        harlow@tom.example
      </li>
      <li class="contact-item">
        <svg class="contact-icon" viewBox="0 0 32 30"><rect x="8" y="2" width="16" height="26" rx="3" fill="none" stroke="#fff" stroke-width="3"/><circle cx="16" cy="23" r="1.8" fill="#fff"/></svg>
        1-555-318-7062
      </li>
      <li class="contact-item">
        <svg class="contact-icon" viewBox="0 0 32 30"><circle cx="16" cy="15" r="13" fill="#fff"/></svg>
        1-555-318-7062
      </li>
      <li class="contact-item">
        <svg class="contact-icon" viewBox="0 0 32 30" fill="none" stroke="#fff" stroke-width="2"><circle cx="16" cy="15" r="13"/><ellipse cx="16" cy="15" rx="6" ry="13"/><path d="M3,15 H29 M5,8 H27 M5,22 H27"/></svg>
        www.sailtideandtime.example
      </li>
    </ul>
  </div>
</body>
</html>
```